RUV Coffee bag (front and back)

We use black matte bags and have front and back labels. We have a logo but need an attractive and inviting label. The labels will be used for our entire line of coffees. We sell most of our coffee to foodservice establishments (Restaurants, Hotels, Bakeries, Bodegas) and we would like to have these establishments display our bags of coffee to sell retail.
The logo can be used as a whole or using any one of the three components (Logo, image, tag).

Target Market(s)

People who buy the coffee they brew at home from the local shop they get their morning latte.. We are a local coffee company, but we do not sell locally roasted coffee!

Industry/Entity Type

Food

Font styles to use
Other font styles liked:
• something that looks good with our trademarked RUV

Colors

Designer to choose colors to be used in the design.

Requirements
Must have
• Respect Trademarked logo
Nice to have
• It would be nice to have a design that can be used with other mediums (airpot wraps, java jackets, )
Should not have
• Real People

```html
<!DOCTYPE html>
<html lang="en">
<head>
<meta charset="utf-8">
<title>RUV Coffee bag labels – front and back</title>
<link rel="stylesheet" href="https://fonts.googleapis.com/css2?family=Cookie&family=Lobster&family=Open+Sans:wght@400;600;700&display=swap">
<style>
  :root {
    --page: #ffffff;
    --bag-black: #151515;
    --ring-grey: #3a3a3a;
    --ring-soft: #2a2a2a;
    --stitch: #b0652a;
    --white: #ffffff;
    --text-light: #e6e6e6;
    --accent-red: #e0161e;
    --crema-light: #c58d55;
    --crema-dark: #6b3d1c;
    --doodle-brown: #4a3322;
  }
  * { box-sizing: border-box; margin: 0; padding: 0; }
  html, body { width: 744px; height: 1200px; overflow: hidden; background: var(--page); }
  .canvas { position: relative; width: 744px; height: 1200px; }
  .label {
    position: absolute; top: 336px; width: 340px; height: 528px;
    background: radial-gradient(ellipse at 50% 40%, #1e1e1e 0%, var(--bag-black) 70%);
    border-radius: 16px; overflow: hidden;
    font-family: "Open Sans", sans-serif; color: var(--text-light);
  }
  .label--front { left: 20px; }
  .label--back { left: 384px; }
  .label__art { position: absolute; inset: 0; width: 100%; height: 100%; }
  .label__stitch {
    position: absolute; inset: 9px; border: 1px dashed var(--stitch); border-radius: 8px; pointer-events: none;
  }
  .doodles {
    position: absolute; left: 0; right: 0; bottom: 0; height: 120px;
    background: linear-gradient(to top, rgba(74,51,34,0.55), rgba(74,51,34,0));
  }
  .product-name {
    position: absolute; left: 50px; top: 92px; width: 260px;
    font-family: "Cookie", cursive; font-weight: 400; color: var(--white); line-height: 0.74;
    text-shadow: 2px 2px 0 #000;
  }
  .product-name span { display: block; }
  .product-name .pn-first { font-size: 80px; padding-left: 118px; }
  .product-name .pn-second { font-size: 70px; padding-left: 4px; }
  .product-name .pn-third { font-size: 70px; padding-left: 62px; }
  .brand { position: absolute; display: flex; flex-direction: column; align-items: center; }
  .brand__dot { width: 26px; height: 26px; border-radius: 50%; background: var(--accent-red); margin-bottom: 6px; }
  .brand__name { font-weight: 400; color: var(--white); letter-spacing: 2px; line-height: 1; }
  .brand__tag { font-size: 5px; letter-spacing: 2px; color: var(--text-light); margin-top: 3px; white-space: nowrap; }
  .label--front .brand { left: 24px; top: 384px; width: 130px; }
  .label--front .brand__dot { width: 40px; height: 40px; margin-bottom: 10px; }
  .label--front .brand__name { font-size: 44px; }
  .label--back .brand { left: 0; right: 0; top: 370px; }
  .label--back .brand__name { font-size: 30px; }
  .fineprint { font-size: 5.2px; line-height: 1.45; color: var(--text-light); }
  .label--front .fineprint { position: absolute; left: 196px; top: 432px; width: 112px; }
  .roast { position: absolute; left: 196px; top: 468px; font-size: 10px; line-height: 1.35; color: var(--white); }
  .roast strong { font-weight: 700; }
  .care { position: absolute; left: 70px; right: 60px; top: 104px; text-align: center; }
  .care__heading {
    font-family: "Lobster", cursive; color: var(--accent-red); font-size: 32px; line-height: 1.05; font-weight: 400;
  }
  .care__heading + p { margin-top: 2px; }
  .care p { font-size: 7.4px; line-height: 1.45; color: var(--white); }
  .care hr { border: 0; height: 0.6px; width: 110px; margin: 5px auto; background: var(--accent-red); }
  .care__storing { margin-top: 24px; }
  .label--back .fineprint { position: absolute; left: 0; right: 0; top: 452px; text-align: center; }
</style>
</head>
<body>
<main class="canvas">

  <section class="label label--front" aria-label="Front label">
    <svg class="label__art" viewBox="0 0 340 528">
      <defs>
        <radialGradient id="cupFill" cx="35%" cy="55%" r="70%">
          <stop offset="0" stop-color="#2a1a10"/>
          <stop offset="0.55" stop-color="#1a1310"/>
          <stop offset="1" stop-color="#0c0c0c"/>
        </radialGradient>
        <linearGradient id="cremaEdge" x1="0" x2="1">
          <stop offset="0" stop-color="var(--crema-light)"/>
          <stop offset="0.45" stop-color="var(--crema-dark)" stop-opacity="0.6"/>
          <stop offset="1" stop-color="#0c0c0c" stop-opacity="0"/>
        </linearGradient>
        <path id="taglineArc" d="M 90 330 Q 176 378 270 322"/>
      </defs>
      <circle cx="176" cy="215" r="208" fill="none" stroke="var(--ring-soft)" stroke-width="22"/>
      <circle cx="176" cy="200" r="160" fill="none" stroke="var(--ring-grey)" stroke-width="18"/>
      <circle cx="176" cy="185" r="126" fill="var(--white)"/>
      <g role="img" aria-label="Top view of an espresso cup with golden crema">
        <circle cx="180" cy="188" r="120" fill="url(#cupFill)"/>
        <circle cx="180" cy="188" r="120" fill="url(#cremaEdge)" opacity="0.85"/>
      </g>
      <text font-family="Open Sans, sans-serif" font-size="10.5" letter-spacing="1.6" fill="#e6e6e6">
        <textPath href="#taglineArc" startOffset="50%" text-anchor="middle">A rich, classic espresso blend.</textPath>
      </text>
    </svg>
    <div class="doodles" role="img" aria-label="Sketched coffee cups and beans pattern"></div>
    <h1 class="product-name"><span class="pn-first">fine</span><span class="pn-second">velvet</span><span class="pn-third">espresso</span></h1>
    <div class="brand">
      <span class="brand__dot"></span>
      <span class="brand__name">RUV</span>
      <span class="brand__tag">Rivers Union Varietals</span>
    </div>
    <p class="fineprint">Lorem ipsum dolor sit amet, consectetuer adipiscing elit, sed diam nonummy nibh euismod tincidunt ut laoreet dolore magna aliquam erat volutpat.</p>
    <p class="roast"><strong>ESPRESSO ROAST</strong><br>2Lb. Whole Bean Coffee</p>
    <div class="label__stitch"></div>
  </section>

  <section class="label label--back" aria-label="Back label">
    <svg class="label__art" viewBox="0 0 340 528" aria-hidden="true">
      <circle cx="171" cy="200" r="200" fill="none" stroke="var(--ring-soft)" stroke-width="20"/>
      <circle cx="171" cy="181" r="150" fill="none" stroke="var(--ring-grey)" stroke-width="14"/>
      <path d="M 88 95 A 120 120 0 0 0 150 300" fill="none" stroke="var(--ring-grey)" stroke-width="10"/>
    </svg>
    <div class="doodles" role="img" aria-label="Sketched coffee cups and beans pattern"></div>
    <div class="care">
      <h2 class="care__heading">Brewing</h2>
      <p>Use freash filtered cold water.</p>
      <hr>
      <p>Measure 2 TBSP of coffee for<br>every 6 oz of water.</p>
      <hr>
      <p>Brew with water 195°F - 205°F</p>
      <h2 class="care__heading care__storing">Storing</h2>
      <p>Store in an airtight container<br>in a cool, dry place</p>
      <hr>
      <p>Do not freeze.</p>
    </div>
    <div class="brand">
      <span class="brand__dot"></span>
      <span class="brand__name">RUV</span>
      <span class="brand__tag">Rivers Union Varietals</span>
    </div>
    <p class="fineprint">Lorem ipsum dolor sit amet, consectetuer<br>adipiscing elit, sed diam nonummy nibh<br>euismod tincidunt ut laoreet dolore magna<br>aliquam erat volutpat.</p>
    <div class="label__stitch"></div>
  </section>

</main>
</body>
</html>
```